Harbor fairly.com a website to help those harmed by lending institutions

I am looking for a basic one page website that will be used to collect data from people filling out a form.
I will need certain key words to be optimized in order for the page to show up as high as possible in the search engines.

This web page is for people that have been harmed by their. Bank or lending institution due to inappropriate accounting practices or worse purposeful neglect.

Imagery should include an elderly person on the phone in distress because of over due bills.

Images of late notices
Images of threats of foreclosure.

** This site is to help people that are being unfairly treated even though they have made all their payments on time and the bank is commiting gross negligence.***

Some basic notes to start:

The color scheme should be similar to this site:

https://www.lendwatchry.com/

Here are some basic notes.

There will be more to follow.

There will need to be a collection form that people can link to and share their story.

Have you or someone you loved been hurt by their financial lending institution?

Have they/ you made all your payments on time only to constantly receive late notice penalties and additional accrued interest ?
Has your credit and good name been tarnished because your banks negligent or purposeful mis-handling of your account has caused the credit bureaus to drop your credit score?
Do you spend hours each month calling your bank to have them clear up their accounting mistakes?
Have you received threatening foreclosure notices even though you've made every payment on time ?

Well if so, you are not alone! This practise or gross incompetence is happening to many others just like you.

Your mortgage, student loan out other debt may have been sold to a new company that simply keeps losing the payments and you have to constantly clear you their errors on your time over and over again.

Budget is flexible based on design.

```html
<!DOCTYPE html>
<html lang="en">
<head>
<meta charset="utf-8">
<title>Harbor fairly – Help for people harmed by lending institutions</title>
<link href="https://fonts.googleapis.com/css2?family=Exo+2:wght@400;500;600;700&family=Open+Sans:wght@400;600&display=swap" rel="stylesheet">
<style>
:root{
  --green:#1b9a6d;
  --green-dark:#12805a;
  --orange:#ee7f22;
  --ink:#111111;
  --text:#333333;
  --grey-bg:#efefef;
  --white:#ffffff;
  --footer:#141414;
}
*{box-sizing:border-box;margin:0;padding:0}
html,body{width:1200px;height:3571px;overflow:hidden}
body{position:relative;background:var(--white);font-family:"Open Sans",sans-serif;color:var(--text)}
.abs{position:absolute}
.heading{font-family:"Exo 2",sans-serif;font-weight:700;color:var(--ink);text-align:center;left:0;width:1200px}

/* header */
.site-header{position:absolute;left:0;top:0;width:1200px;height:124px;background:var(--white);border-bottom:6px solid var(--orange);z-index:3}
.brand{position:absolute;left:74px;top:38px;font-family:"Exo 2",sans-serif;font-weight:600;font-size:44px;color:var(--green);letter-spacing:-.5px}
.contact-pill{position:absolute;left:805px;top:10px;width:319px;height:31px;background:var(--green);border-radius:8px;color:var(--white);font-family:"Exo 2",sans-serif;font-size:14px;display:flex;align-items:center;justify-content:center;gap:26px}
.contact-pill span{display:flex;align-items:center;gap:8px}
.main-nav{position:absolute;top:72px;left:0;width:1200px;font-family:"Exo 2",sans-serif;font-weight:600;font-size:17px;color:var(--ink)}
.main-nav a{position:absolute;color:inherit;text-decoration:none;white-space:nowrap}
.main-nav a.active{color:var(--orange)}

.social-rail{position:absolute;left:1148px;top:107px;z-index:4;display:flex;flex-direction:column;gap:10px}
.dot{width:38px;height:38px;border-radius:50%;display:block}
.dot.s1{background:#1c3f9e}.dot.s2{background:#1e9be6}.dot.s3{background:#d0246a}.dot.s4{background:#e01717}

/* hero */
.hero-photo{position:absolute;left:0;top:124px;width:1200px;height:640px;background:linear-gradient(100deg,#bdbdbd 0%,#8a8a8a 30%,#d8d8d8 55%,#6f6f6f 80%,#a9a9a9 100%)}
.contact-panel{position:absolute;left:802px;top:186px;width:322px;height:421px;background:var(--green)}
.contact-panel h2{font-family:"Exo 2",sans-serif;font-weight:600;font-size:25px;color:var(--white);text-align:center;margin-top:32px}
.panel-field{position:absolute;left:27px;width:269px;height:36px;background:var(--white);font-family:"Exo 2",sans-serif;font-size:13px;color:#444;padding:11px 12px}
.btn{position:absolute;background:var(--orange);color:var(--white);font-family:"Exo 2",sans-serif;font-weight:600;display:flex;align-items:center;justify-content:center;clip-path:polygon(8% 0,100% 0,92% 100%,0 100%)}
.slider-arrow{position:absolute;top:686px;width:38px;height:38px;border-radius:50%;background:var(--ink)}

/* welcome */
.welcome-text{position:absolute;left:134px;top:910px;width:932px;font-size:12.6px;line-height:23px;text-align:center;color:var(--text)}

/* how we help */
.help-copy{position:absolute;left:190px;width:820px;text-align:center;color:var(--white)}
.photo{position:absolute;overflow:hidden}
.photo-tag{position:absolute;left:0;bottom:21px;width:265px;height:50px;background:var(--orange);color:var(--white);font-family:"Exo 2",sans-serif;font-weight:600;font-size:28px;padding:8px 0 0 50px;clip-path:polygon(0 0,88% 0,100% 50%,88% 100%,0 100%)}

/* services */
.service-card{position:absolute;top:1964px;width:246px;height:169px}
.service-caption{position:absolute;top:2142px;width:246px;text-align:center;font-family:"Exo 2",sans-serif;font-weight:600;font-size:17px;color:var(--ink)}
.pager span{position:absolute;top:2219px;width:13px;height:13px;border-radius:50%;background:var(--green)}
.pager span.on{background:var(--orange)}

/* testimonial */
.testimonial{position:absolute;left:138px;top:2393px;width:924px;height:255px;background:var(--orange);color:var(--white);text-align:center}
.quote-badge{position:absolute;left:562px;top:2360px;width:66px;height:66px;border-radius:50%;background:var(--white)}
.testimonial p{position:absolute;left:70px;top:65px;width:784px;font-size:14px;line-height:25px}
.testimonial .name{position:absolute;left:0;width:924px;top:160px;font-family:"Exo 2",sans-serif;font-size:21px}
.testimonial .role{position:absolute;left:0;width:924px;top:193px;font-family:"Exo 2",sans-serif;font-size:14px}

/* contact */
.contact-field{position:absolute;background:var(--white);border:1px solid #bdbdbd;font-family:"Exo 2",sans-serif;font-size:13px;color:#444;padding:11px 14px}
.robot-check{position:absolute;left:262px;top:3157px;width:205px;height:50px;background:#f9f9f9;border:1px solid #d3d3d3;font-size:11px;color:#222;display:flex;align-items:center;gap:10px;padding-left:12px}
.robot-check i{width:20px;height:20px;border:2px solid #c1c1c1;background:var(--white);display:block}
.robot-check b{margin-left:auto;margin-right:12px;width:26px;height:26px;border-radius:50%;background:#4a7bd8;display:block}

/* footer */
.site-footer{position:absolute;left:0;top:3264px;width:1200px;height:307px;background:var(--footer);color:var(--white)}
.footer-brand{position:absolute;left:0;width:1200px;top:50px;text-align:center;font-family:"Exo 2",sans-serif;font-weight:600;font-size:40px;color:var(--green)}
.footer-nav{position:absolute;left:0;width:1200px;top:123px;display:flex;justify-content:center;gap:38px;font-family:"Exo 2",sans-serif;font-weight:600;font-size:16px}
.footer-social{position:absolute;left:512px;top:184px;display:flex;gap:8px}
.copyright{position:absolute;left:0;width:1200px;top:252px;text-align:center;font-size:13px}
</style>
</head>
<body>

<header class="site-header">
  <div class="brand">harborfairly</div>
  <div class="contact-pill">
    <span><svg width="14" height="14" viewBox="0 0 24 24"><path fill="#fff" d="M6.6 10.8a15 15 0 0 0 6.6 6.6l2.2-2.2c.3-.3.7-.4 1-.2 1.1.4 2.3.6 3.6.6.6 0 1 .4 1 1V20c0 .6-.4 1-1 1A17 17 0 0 1 3 4c0-.6.4-1 1-1h3.5c.6 0 1 .4 1 1 0 1.3.2 2.5.6 3.6.1.3 0 .7-.2 1z"/></svg>1-800 555 0142</span>
    <span><svg width="14" height="12" viewBox="0 0 24 18"><rect width="24" height="18" rx="2" fill="#fff"/><path d="M1 2l11 8 11-8" stroke="#1b9a6d" stroke-width="2" fill="none"/></svg>info@harborfairly.com</span>
  </div>
  <nav class="main-nav">
    <a class="active" style="left:522px">Home</a>
    <a style="left:597px">About Us</a>
    <a style="left:700px">How we help</a>
    <a style="left:830px">Services</a>
    <a style="left:928px">Tetimonials</a>
    <a style="left:1045px">Contact Us</a>
  </nav>
</header>

<div class="social-rail">
  <span class="dot s1"></span><span class="dot s2"></span><span class="dot s3"></span><span class="dot s4"></span>
</div>

<section class="hero">
  <div class="hero-photo" role="img" aria-label="Black and white photo of an elderly couple smiling together at home"></div>
  <svg class="abs" style="left:0;top:650px" width="1200" height="120" viewBox="0 0 1200 120">
    <polygon points="660,66 1200,18 1200,92 0,112" fill="#ee7f22"/>
    <polygon points="0,112 1200,92 1200,120 0,120" fill="#fff"/>
  </svg>
  <form class="contact-panel">
    <h2>GET IN TOUCH</h2>
    <div class="panel-field" style="top:78px">Name</div>
    <div class="panel-field" style="top:126px">Phone Number</div>
    <div class="panel-field" style="top:174px">Email</div>
    <div class="panel-field" style="top:222px">Address</div>
    <div class="panel-field" style="top:270px">Type of Issue</div>
    <div class="panel-field" style="top:318px">Type of organisation</div>
  </form>
  <div class="btn" style="left:862px;top:574px;width:202px;height:50px;font-size:24px">Submit</div>
  <div class="slider-arrow" style="left:1036px"><svg width="38" height="38"><polygon points="23,12 13,19 23,26" fill="#fff"/></svg></div>
  <div class="slider-arrow" style="left:1086px"><svg width="38" height="38"><polygon points="15,12 25,19 15,26" fill="#fff"/></svg></div>
</section>

<section class="welcome">
  <h1 class="heading abs" style="top:822px;font-size:50px">Welcome To Harborfairly</h1>
  <p class="welcome-text">Lorem ipsum dolor sit amet, consectetur adipiscing elit, sed do eiusmod tempor incididunt ut labore et dolore magna aliqua. Ut enim ad minim veniam, quis nostrud exercitation ullamco laboris nisi ut aliquip ex ea commodo consequat. Duis aute irure dolor in reprehenderit in voluptate velit esse cillum dolore eu fugiat nulla pariatur. Excepteur sint occaecat cupidatat non proident, sunt in culpa qui officia deserunt mollit anim id est laborum</p>
  <div class="btn" style="left:495px;top:1007px;width:210px;height:53px;font-size:22px">Read more</div>
</section>

<section class="help">
  <svg class="abs" style="left:0;top:1100px" width="1200" height="770" viewBox="0 0 1200 770">
    <polygon points="0,7 1200,65 1200,690 0,762" fill="#1b9a6d"/>
    <polygon points="0,572 1200,566 1200,690 0,762" fill="#12805a"/>
    <polygon points="584,724 616,724 600,754" fill="#1b9a6d"/>
  </svg>
  <h2 class="heading abs" style="top:1712px;font-size:48px;color:var(--white)">Services</h2>
  <h2 class="heading abs" style="top:1214px;font-size:50px;color:var(--white)">How we Help</h2>
  <div class="help-copy" style="top:1318px;font-family:'Exo 2',sans-serif;font-weight:600;font-size:22px">Lorem Ipsum passage</div>
  <p class="help-copy" style="top:1359px;font-size:16px;line-height:23px">Lorem ipsum dolor sit amet, consectetur adipiscing elit, sed do eiusmod tempor incididunt ut labore et dolore magna aliqua. Ut enim ad minim veniam</p>
  <div class="photo" style="left:160px;top:1450px;width:428px;height:219px">
    <div style="width:100%;height:100%;background:linear-gradient(120deg,#b9b2a8,#e7e3dd 55%,#8f8679)" role="img" aria-label="Elderly couple sitting on a sofa with cups"></div>
    <div class="photo-tag">Bonorum</div>
  </div>
  <div class="photo" style="left:614px;top:1450px;width:426px;height:219px">
    <div style="width:100%;height:100%;background:linear-gradient(110deg,#e4e4e4,#b1a89d 45%,#2b2f3a 80%)" role="img" aria-label="Older couple meeting an advisor reviewing documents"></div>
    <div class="photo-tag">Finibus</div>
  </div>
</section>

<section class="services">
  <p class="abs" style="left:190px;top:1880px;width:820px;text-align:center;font-size:16.5px;line-height:23px">Sed ut perspiciatis unde omnis iste natus error sit voluptatem accusantium doloremque laudantium, totam rem aperiam, eaque ipsa quae ab illo inventore veritatis et quasi architecto beatae vitae</p>
  <div class="service-card" style="left:93px;background:linear-gradient(135deg,#e9eef2,#9fb2c4)" role="img" aria-label="Hands working through bills with a calculator"></div>
  <div class="service-card" style="left:350px;background:linear-gradient(135deg,#c2621c,#7a3a12)" role="img" aria-label="Elderly couple looking at a tablet"></div>
  <div class="service-card" style="left:605px;background:linear-gradient(135deg,#f4f4f4,#c9c9c9)" role="img" aria-label="Notice of foreclosure paper"></div>
  <div class="service-card" style="left:862px;background:linear-gradient(135deg,#dfe6ee,#3d5a86)" role="img" aria-label="Person reviewing financial charts on a calculator"></div>
  <div class="service-caption" style="left:93px">Reprehenderit</div>
  <div class="service-caption" style="left:350px">Consectetur</div>
  <div class="service-caption" style="left:605px">Neque porro</div>
  <div class="service-caption" style="left:862px">Consequuntur</div>
  <div class="pager"><span style="left:551px"></span><span class="on" style="left:580px"></span><span style="left:608px"></span><span style="left:637px"></span></div>
</section>

<section class="testimonials">
  <h2 class="heading abs" style="top:2288px;font-size:50px">Testimonials</h2>
  <div class="testimonial">
    <p>"Sed ut perspiciatis unde omnis iste natus error sit voluptatem accusantium doloremque laudantium, totam rem aperiam, eaque ipsa quae ab illo inventore veritatis et quasi architecto beatae vitae dicta sunt explicabo. Nemo enim ipsam voluptatem quia voluptas sit aspernatur aut odit aut fugit."</p>
    <div class="name">Dana Whitfield</div>
    <div class="role">Director</div>
  </div>
  <div class="quote-badge"><svg width="66" height="66"><text x="33" y="52" text-anchor="middle" font-family="Exo 2, sans-serif" font-weight="700" font-size="44" fill="#111">”</text></svg></div>
</section>

<section class="contact">
  <svg class="abs" style="left:0;top:2695px" width="1200" height="570" viewBox="0 0 1200 570">
    <polygon points="0,98 1200,0 1200,570 0,570" fill="#efefef"/>
  </svg>
  <h2 class="heading abs" style="top:2812px;font-size:48px">Call or Contact Us Today!</h2>
  <div class="heading abs" style="top:2886px;font-size:36px">1-800 555 0199</div>
  <div class="contact-field" style="left:262px;top:2969px;width:319px;height:41px">NAME</div>
  <div class="contact-field" style="left:593px;top:2969px;width:321px;height:41px">EMAIL</div>
  <div class="contact-field" style="left:262px;top:3029px;width:652px;height:111px">MESSAGE</div>
  <div class="robot-check"><i></i>I'm not a robot<b></b></div>
  <div class="btn" style="left:736px;top:3157px;width:178px;height:50px;font-size:19px">SUBMIT</div>
</section>

<footer class="site-footer">
  <div class="footer-brand">harborfairly</div>
  <nav class="footer-nav"><span>Home</span><span>About Us</span><span>How we help</span><span>Services</span><span>Tetimonials</span><span>Contact Us</span></nav>
  <div class="footer-social"><span class="dot s1"></span><span class="dot s2"></span><span class="dot s3"></span><span class="dot s4"></span></div>
  <div class="copyright">© 2019 &nbsp;|&nbsp; www.harborfairly.com</div>
</footer>

</body>
</html>
```